Website for designing and selling name-labels

We are looking for a fresh design for a site similar to these (www.sivrekana.no, www.tumbelorra.no, www.hesketrim.no) where the consumer can come online designing their own labels (30x15 mm) , either with onlye text or with text, choose a pre-defined symbol (which we have) and/or a color. We will the print the labels on our side, and send it to the customer.

We are looking for the front page, product page and check out - page.

Target Market(s)

families with childring, scools, kinder garden, industry

Number of Pages Required

3 page

Requirements
Nice to have
• bright and easy design
easy to design and see their own designs
easy check out - few steps

```html
<!DOCTYPE html>
<html lang="en">
<head>
<meta charset="utf-8">
<title>Labeltun – Design your own product</title>
<link rel="stylesheet" href="https://fonts.googleapis.com/css2?family=Poppins:ital,wght@0,400;0,500;0,600;0,700;1,400&family=Lato:wght@700;900&family=Open+Sans:wght@600&display=swap">
<style>
:root{
  --teal:#23897e;
  --teal-dark:#0e3f39;
  --teal-band:#25897f;
  --hero-bg:#ececee;
  --ink:#222;
  --muted:#777;
  --line:#e2e2e2;
  --white:#fff;
}
*{box-sizing:border-box;margin:0;padding:0}
html,body{width:1200px;height:2806px;overflow:hidden;background:var(--white)}
body{position:relative;font-family:"Poppins",sans-serif;color:var(--ink)}
.abs{position:absolute}
a{color:inherit;text-decoration:none}

/* header */
.brand{left:144px;top:16px;width:184px;height:51px;background:var(--teal);border-radius:6px;color:var(--white);font:700 15px/51px "Poppins",sans-serif;text-align:center;letter-spacing:.5px}
.top-info{top:30px;font-size:16px;color:#333}
.cart{left:989px;top:24px;width:66px;height:35px;border-radius:18px;background:var(--teal)}
.nav{left:0;top:82px;width:1200px;height:51px;border-top:1px solid var(--line);border-bottom:1px solid var(--line);box-shadow:0 2px 4px rgba(0,0,0,.06)}
.nav a{position:absolute;top:16px;font-size:13px;color:#333}

/* hero */
.hero{left:0;top:133px;width:1200px;height:500px;background:var(--hero-bg);overflow:hidden}
.hero-title{left:220px;top:128px;font:600 58px/1 "Poppins",sans-serif;color:var(--teal-dark);letter-spacing:-1px}
.hero-sub{left:221px;top:220px;font-size:24px;letter-spacing:14px;color:var(--teal-dark)}
.btn-solid{left:222px;top:274px;width:134px;height:41px;background:var(--teal);color:var(--white);font:600 16px/41px "Open Sans",sans-serif;text-align:center}
.toys{left:0;top:270px;width:430px;height:230px;background:linear-gradient(100deg,#e7a24a,#d9434a 45%,#f1d24b 70%,#49b9c9);border-radius:120px 140px 0 0;opacity:.85}
.bottles{left:630px;top:38px;width:330px;height:372px;background:linear-gradient(90deg,#2146c9 0%,#eaeaea 45%,#2b2b2b 70%,#111 100%);border-radius:60px 60px 30px 30px}
.dots{left:506px;top:428px;width:189px;height:72px;background:var(--teal);border-radius:95px 95px 0 0}

/* category grid */
.tile{overflow:hidden;color:var(--white);font-family:"Lato",sans-serif;font-weight:900}
.tile .l1{position:absolute;left:34px;font-size:62px;line-height:1}
.tile .l2{position:absolute;left:34px;font-size:62px;line-height:1;letter-spacing:22px}

/* about band */
.about{left:0;top:1324px;width:1200px;height:407px;background:var(--teal-band);text-align:center;color:var(--white)}
.about h2{position:absolute;top:52px;width:100%;font:600 64px/1.1 "Poppins",sans-serif}
.about p{position:absolute;left:185px;top:146px;width:830px;font:700 16px/30px "Lato",sans-serif}
.btn-outline{position:absolute;left:515px;top:298px;width:170px;height:44px;border:1px solid var(--white);font:600 16px/42px "Open Sans",sans-serif}
.bear-l,.bear-r{position:absolute;top:60px;width:220px;height:300px;background:rgba(255,255,255,.05);border-radius:110px}
.bear-l{left:10px}.bear-r{right:10px}

/* testimonials */
.deco-a{left:0;top:1770px;width:390px;height:190px;background:linear-gradient(100deg,rgba(231,162,74,.25),rgba(217,67,74,.2),rgba(241,210,75,.2));border-radius:100px 120px 0 0}
.deco-b{left:960px;top:2265px;width:240px;height:180px;background:linear-gradient(100deg,rgba(241,210,75,.2),rgba(217,67,74,.2),rgba(231,162,74,.25));border-radius:100px 110px 0 0}
.t-title{left:0;top:1818px;width:1200px;text-align:center;font:600 46px/1.1 "Poppins",sans-serif;color:#111}
.t-sub{left:0;top:1890px;width:1200px;text-align:center;font:italic 17px "Poppins",sans-serif;color:#555}
.card{left:144px;top:1960px;width:912px;height:333px;background:var(--white);box-shadow:0 2px 12px rgba(0,0,0,.12)}
.quote-mark{position:absolute;left:48px;top:36px}
.quote{position:absolute;left:48px;top:106px;width:570px;font:italic 19px/29px "Poppins",sans-serif;color:#777}
.person{position:absolute;left:54px;top:230px;font-size:22px;color:var(--teal)}
.place{position:absolute;left:54px;top:270px;font-size:16px;color:#444}
.portrait{position:absolute;left:662px;top:0;width:250px;height:333px;background:linear-gradient(180deg,#e7e2d8,#d8b8a8 60%,#cfd4de)}
.arrow{width:34px;height:34px;border-radius:50%}

/* newsletter + footer */
.footer{left:0;top:2445px;width:1200px;height:361px;background:var(--teal)}
.news{left:146px;top:2365px;width:909px;height:125px;background:var(--teal);border:3px solid var(--white)}
.news h3{position:absolute;left:64px;top:40px;font:400 30px "Poppins",sans-serif;color:var(--white)}
.news .field{position:absolute;left:412px;top:42px;width:283px;height:38px;background:var(--white);border:1px solid #ccc;font-size:14px;color:#888;padding:9px 14px}
.news .go{position:absolute;left:704px;top:42px;width:134px;height:38px;border:1px solid var(--white);color:var(--white);text-align:center;font:500 18px/36px "Poppins",sans-serif}
.f-brand{left:144px;top:2545px;width:244px;height:66px;border:1px solid rgba(255,255,255,.4);border-radius:6px;color:var(--white);font:700 17px/64px "Poppins",sans-serif;text-align:center}
.social{width:28px;height:28px;border:1.5px solid var(--white);border-radius:50%;top:2630px}
.f-col{top:2548px;color:var(--white)}
.f-col h4{font:500 13px "Poppins",sans-serif;letter-spacing:.5px;margin-bottom:12px}
.f-col li{list-style:none;font-size:12.5px;line-height:24px}
.f-div{top:2548px;width:1px;height:210px;background:rgba(255,255,255,.6)}
.f-rule{left:144px;top:2748px;width:912px;height:1px;background:rgba(255,255,255,.6)}
.copy{left:0;top:2770px;width:1200px;text-align:center;color:var(--white);font-size:13px}
</style>
</head>
<body>

<header>
  <div class="abs brand">LABELTUN.NO</div>
  <div class="abs top-info" style="left:693px">100% Free Shipping</div>
  <div class="abs top-info" style="left:871px">Get 20% Off</div>
  <div class="abs cart">
    <svg width="66" height="35" viewBox="0 0 66 35"><path d="M25 10h3l3 10h10l3-7H30" fill="none" stroke="#fff" stroke-width="2.2"/><circle cx="32" cy="24" r="1.8" fill="#fff"/><circle cx="40" cy="24" r="1.8" fill="#fff"/></svg>
  </div>
  <nav class="abs nav">
    <a style="left:142px">Name tags</a>
    <a style="left:283px">Minilapper</a>
    <a style="left:420px">Ironing pads</a>
    <a style="left:571px">Temalapper</a>
    <a style="left:720px">MY ID</a>
    <a style="left:824px">Drinking bottle</a>
    <a style="left:988px">Contact Us</a>
  </nav>
</header>

<section class="abs hero">
  <div class="abs toys" role="img" aria-label="Colourful children's toys: teddy bear, rocket, helicopter and stacking rings"></div>
  <div class="abs bottles" role="img" aria-label="Labelled drinking bottles in blue, white and black"></div>
  <h1 class="abs hero-title">Design your Own</h1>
  <div class="abs hero-sub">PRODUCT</div>
  <a class="abs btn-solid">Order Now</a>
  <div class="abs dots">
    <svg width="189" height="72"><circle cx="53" cy="36" r="8" fill="#1a5e56"/><circle cx="80" cy="36" r="11" fill="#153f3a"/><circle cx="109" cy="36" r="8" fill="#1a5e56"/><circle cx="137" cy="36" r="8" fill="#1a5e56"/></svg>
  </div>
</section>

<section>
  <div class="abs tile" style="left:144px;top:696px;width:446px;height:272px;background:linear-gradient(90deg,#151515,#6a6a6a 45%,#b01c1c 60%,#c9c9c9)" role="img" aria-label="Red metal drink flasks">
    <span class="l1" style="top:105px">DRINK</span><span class="l2" style="top:175px">FLASK</span>
  </div>
  <div class="abs tile" style="left:144px;top:986px;width:446px;height:272px;background:linear-gradient(120deg,#2a2f1e,#4f4a2a 40%,#b8343a 70%,#1b1f15)" role="img" aria-label="Knitted baby booties with bear faces">
    <span class="l1" style="top:105px">BABY</span><span class="l2" style="top:175px">TOYS</span>
  </div>
  <div class="abs tile" style="left:610px;top:696px;width:446px;height:562px;background:linear-gradient(160deg,#e8a32a,#d97fae 40%,#9a6f86 70%,#3b3734)" role="img" aria-label="Plush teddy bears in yellow, pink and panda colours">
    <span class="l1" style="left:45px;top:380px">NAME</span><span class="l2" style="left:45px;top:450px">TAGS</span>
  </div>
</section>

<section class="abs about">
  <div class="bear-l" role="img" aria-label="Faint teddy bear"></div>
  <div class="bear-r" role="img" aria-label="Faint teddy bear"></div>
  <h2>Labeltun</h2>
  <p>Lorem Ipsum is simply dummy text of the printing and typesetting industry. Lorem Ipsum has been the industry's standard dummy text ever since the 1500s, when an unknown printer took a galley of type and scrambled it to make a type specimen book. It has survived not only five centuries, but also the leap into electronic typesetting, remaining essentially unchanged.</p>
  <a class="btn-outline">Read More</a>
</section>

<section>
  <div class="abs deco-a" role="img" aria-label="Faint toys decoration"></div>
  <div class="abs deco-b" role="img" aria-label="Faint toys decoration"></div>
  <h2 class="abs t-title">Testimonials</h2>
  <p class="abs t-sub">Lorem Ipsum is simply dummy text of the printing and typesetting</p>
  <div class="abs card">
    <svg class="quote-mark" width="46" height="40" viewBox="0 0 46 40"><path d="M2 38V18Q2 4 18 2v8Q10 12 10 18h8v20zM26 38V18Q26 4 42 2v8Q34 12 34 18h8v20z" fill="var(--teal)"/></svg>
    <p class="quote">Lorem Ipsum is simply dummy text of the printing and typesetting industry. Lorem Ipsum has been the industry's standard dummy text ever since the 1500s, when an unknown printer took a galley of type and</p>
    <div class="person">Henrik Dalsvik</div>
    <div class="place">FJORDLYS HOTEL. 2021</div>
    <div class="portrait" role="img" aria-label="Portrait of a smiling customer"></div>
  </div>
  <div class="abs arrow" style="left:127px;top:2109px;background:#9fcdc7">
    <svg width="34" height="34"><path d="M19 11l-6 6 6 6" fill="none" stroke="#fff" stroke-width="2"/></svg>
  </div>
  <div class="abs arrow" style="left:1038px;top:2109px;background:var(--teal)">
    <svg width="34" height="34"><path d="M15 11l6 6-6 6" fill="none" stroke="#fff" stroke-width="2"/></svg>
  </div>
</section>

<footer>
  <div class="abs footer"></div>
  <div class="abs news">
    <h3>Sign up for newsletter</h3>
    <div class="field">Your Email</div>
    <div class="go">SIGN UP</div>
  </div>
  <div class="abs f-brand">LABELTUN.NO</div>
  <div class="abs social" style="left:203px"></div>
  <div class="abs social" style="left:236px"></div>
  <div class="abs social" style="left:268px"></div>
  <div class="abs social" style="left:301px"></div>
  <div class="abs f-col" style="left:470px"><h4>PRODUCTS</h4><ul><li>Name tags</li><li>Name tags with familiar figures</li><li>Minilapper</li><li>Large name tags</li><li>Ironing pads</li><li>Door decoration</li></ul></div>
  <div class="abs f-div" style="left:694px"></div>
  <div class="abs f-col" style="left:745px"><h4>HELPFUL LINKS</h4><ul><li>Search</li><li>FAQ's</li><li>Contact Us</li><li>Careers</li><li>Resources</li><li>Privacy Policy</li></ul></div>
  <div class="abs f-div" style="left:909px"></div>
  <div class="abs f-col" style="left:954px"><h4>MAIN MENU</h4><ul><li>Name tags</li><li>Minilapper</li><li>Ironing pads</li><li>Temalapper</li><li>MY ID</li><li>Drinking bottle</li></ul></div>
  <div class="abs f-rule"></div>
  <div class="abs copy">Labeltun © 2021 All Rights Reserved.</div>
</footer>

</body>
</html>
```